Email Newsletter for Dentists includes coding

We supply to professional market of doctors and dentists.
German Quality and good price is the message we want to give
Gallery style newsletter to include all the code to link to web products.
Professional look, use creative clinical style.
Please see the pdf draft. It needs creative attention.
If you need original images or other content let us know, and we can upload.
You can see the links in the plain black font size 2.
Our website is calvorix.com.au please go there see our concepts of business.
Updates

Please note:Use the correct size for email news letter.I have included some old examples of newsletter we did before. But you can see our logo has changed and we now adopt a blue theme.You can see not much text just rpice icons and simple white background. Dont over complicate it with fancy backgrounds or too much text. Added Saturday, March 26, 2016

Target Market(s)

Dentists and Doctors

Industry/Entity Type

Medical Equipment

Coding

Coded - Design and coding required

Requirements
Must have
• Coded and Gallery Style
• Looks professional
• The design should fit so no scrollbars needed to view the entire email.
• All the products shown in the draft
• Use only the blue logo design and theme.
Nice to have
• Use your creative design
Should not have
• No Clipart
• No Stock Images
• No Scroll Bars when viewing the newsletter.

```html
<!DOCTYPE html>
<html lang="en">
<head>
<meta charset="utf-8">
<title>Calvorix Newsletter</title>
<link href="https://fonts.googleapis.com/css2?family=Open+Sans:wght@400;600;700&family=Roboto:wght@400&display=swap" rel="stylesheet">
<style>
:root{
  --page:#f3f3f3;
  --white:#ffffff;
  --blue:#2476c2;
  --hero:#3d86c6;
  --red:#d0021b;
  --ink:#222222;
  --muted:#7a7a7a;
  --line:#dcdcdc;
  --footer:#333333;
}
*{margin:0;padding:0;box-sizing:border-box}
html,body{width:975px;height:1200px;overflow:hidden;background:var(--page);font-family:"Open Sans",Arial,sans-serif;color:var(--ink)}
.preheader{width:650px;margin:0 auto;padding:16px 0 0 2px;height:43px;font:400 10px "Roboto",Arial,sans-serif;color:#555}
.preheader a{color:var(--blue)}
.email{width:650px;margin:0 auto;background:var(--white);border:1px solid var(--line);border-top:3px solid var(--blue);box-shadow:0 6px 10px rgba(0,0,0,.08)}
.header{height:88px;display:flex;align-items:center;padding:0 14px 0 16px}
.brand{font-weight:700;font-size:52px;letter-spacing:-2px;color:#6d6e71;flex:1;line-height:1}
.contact{font-size:13px;color:var(--muted);font-weight:600;padding:0 0 0 16px}
.contact strong{display:block;color:var(--blue);font-weight:600}
.contact.au{padding-right:16px;border-right:1px solid #bbb}
.hero{height:205px;background:linear-gradient(180deg,#4a8fcb,#3a80c1);display:flex;align-items:center;justify-content:center;text-align:center;color:var(--white);font-size:30px;font-weight:600;line-height:42px}
.hero b{font-size:34px;font-weight:700}
.grid{display:grid;grid-template-columns:repeat(3,197px);column-gap:14px;row-gap:35px;padding:36px 15px 34px}
.product{height:287px;border:1px solid var(--line);text-align:center;position:relative;box-shadow:0 8px 8px -6px rgba(0,0,0,.12)}
.product-image{height:114px;border-bottom:1px solid var(--line);background:linear-gradient(135deg,#f7f7f7,#d9dcdf)}
.ribbon{position:absolute;top:-12px;right:2px;width:56px;height:62px}
.product h3{font-size:13px;font-weight:600;line-height:18px;margin:11px 8px 4px}
.price{font-size:18px;font-weight:600;color:var(--blue)}
.buy{display:block;width:119px;height:36px;margin:8px auto 0;background:var(--blue);color:var(--white);font-size:14px;font-weight:600;line-height:36px;text-decoration:none}
.origin{font-size:11px;line-height:14px;margin-top:7px}
.footer{height:100px;background:var(--footer);color:var(--white);display:flex;align-items:center;padding:0 16px}
.footer .brand{color:var(--white);font-size:40px;flex:0 0 209px;border-right:1px solid #aaa;height:70px;display:flex;align-items:center}
.follow{margin-left:110px;text-align:center;font-size:14px;font-weight:600}
.social{display:flex;gap:4px;margin-top:4px}
.social span{width:24px;height:24px;border-radius:50%;background:var(--white)}
.address{margin-left:40px;font-size:12px;line-height:15px;display:flex;gap:8px;align-self:flex-start;margin-top:20px}
.copyright{text-align:center;font-size:11px;color:#444;margin-top:26px}
</style>
</head>
<body>
<div class="preheader">Having trouble viewing this email? <a href="#">View in a browser window</a></div>
<div class="email">
  <header class="header">
    <div class="brand">calvorix</div>
    <div class="contact au">Australia<strong>Call: 1300 482 615</strong></div>
    <div class="contact nz">New Zealand<strong>Call: +617 5590 3174</strong></div>
  </header>
  <section class="hero" role="img" aria-label="Surgical instruments faintly shown behind the headline">
    <p><b>OVER 10,000</b> product lines of surgical,<br>medical and dental instruments<br><b>Available</b></p>
  </section>
  <section class="grid">
    <article class="product"><div class="product-image" role="img" aria-label="Extraction forceps with tip detail"></div><svg class="ribbon" viewBox="0 0 56 62"><path d="M0 0h48l8 10v52L28 48 0 62z" fill="var(--red)"/><text x="28" y="24" text-anchor="middle" fill="#fff" font-family="Open Sans,sans-serif" font-weight="700" font-size="15">50%</text><text x="28" y="38" text-anchor="middle" fill="#fff" font-family="Open Sans,sans-serif" font-weight="700" font-size="11">OFF</text></svg><h3>Extraction Forceps Anterior Incisors and Canines #35</h3><div class="price">$189.50</div><a class="buy" href="#">BUY NOW</a><p class="origin">Country of Manufacture:<br>Germany</p></article>
    <article class="product"><div class="product-image" role="img" aria-label="Extraction forceps with tip detail"></div><svg class="ribbon" viewBox="0 0 56 62"><path d="M0 0h48l8 10v52L28 48 0 62z" fill="var(--red)"/><text x="28" y="24" text-anchor="middle" fill="#fff" font-family="Open Sans,sans-serif" font-weight="700" font-size="15">50%</text><text x="28" y="38" text-anchor="middle" fill="#fff" font-family="Open Sans,sans-serif" font-weight="700" font-size="11">OFF</text></svg><h3>Extraction Forceps Anterior Incisors and Canines #35</h3><div class="price">$189.50</div><a class="buy" href="#">BUY NOW</a><p class="origin">Country of Manufacture:<br>Germany</p></article>
    <article class="product"><div class="product-image" role="img" aria-label="Extraction forceps with tip detail"></div><svg class="ribbon" viewBox="0 0 56 62"><path d="M0 0h48l8 10v52L28 48 0 62z" fill="var(--red)"/><text x="28" y="24" text-anchor="middle" fill="#fff" font-family="Open Sans,sans-serif" font-weight="700" font-size="15">50%</text><text x="28" y="38" text-anchor="middle" fill="#fff" font-family="Open Sans,sans-serif" font-weight="700" font-size="11">OFF</text></svg><h3>Extraction Forceps Anterior Incisors and Canines #35</h3><div class="price">$189.50</div><a class="buy" href="#">BUY NOW</a><p class="origin">Country of Manufacture:<br>Germany</p></article>
    <article class="product"><div class="product-image" role="img" aria-label="Extraction forceps with tip detail"></div><svg class="ribbon" viewBox="0 0 56 62"><path d="M0 0h48l8 10v52L28 48 0 62z" fill="var(--red)"/><text x="28" y="24" text-anchor="middle" fill="#fff" font-family="Open Sans,sans-serif" font-weight="700" font-size="15">50%</text><text x="28" y="38" text-anchor="middle" fill="#fff" font-family="Open Sans,sans-serif" font-weight="700" font-size="11">OFF</text></svg><h3>Extraction Forceps Anterior Incisors and Canines #35</h3><div class="price">$189.50</div><a class="buy" href="#">BUY NOW</a><p class="origin">Country of Manufacture:<br>Germany</p></article>
    <article class="product"><div class="product-image" role="img" aria-label="Dressing tweezers with tip detail"></div><svg class="ribbon" viewBox="0 0 56 62"><path d="M0 0h48l8 10v52L28 48 0 62z" fill="var(--red)"/><text x="28" y="24" text-anchor="middle" fill="#fff" font-family="Open Sans,sans-serif" font-weight="700" font-size="15">50%</text><text x="28" y="38" text-anchor="middle" fill="#fff" font-family="Open Sans,sans-serif" font-weight="700" font-size="11">OFF</text></svg><h3>Extraction Forceps Anterior Incisors and Canines #35</h3><div class="price">$189.50</div><a class="buy" href="#">BUY NOW</a><p class="origin">Country of Manufacture:<br>Germany</p></article>
    <article class="product"><div class="product-image" role="img" aria-label="Angled clamp forceps with tip detail"></div><svg class="ribbon" viewBox="0 0 56 62"><path d="M0 0h48l8 10v52L28 48 0 62z" fill="var(--red)"/><text x="28" y="24" text-anchor="middle" fill="#fff" font-family="Open Sans,sans-serif" font-weight="700" font-size="15">50%</text><text x="28" y="38" text-anchor="middle" fill="#fff" font-family="Open Sans,sans-serif" font-weight="700" font-size="11">OFF</text></svg><h3>Extraction Forceps Anterior Incisors and Canines #35</h3><div class="price">$189.50</div><a class="buy" href="#">BUY NOW</a><p class="origin">Country of Manufacture:<br>Germany</p></article>
  </section>
  <footer class="footer">
    <div class="brand">calvorix</div>
    <div class="follow">Follow Us<div class="social"><span></span><span></span><span></span></div></div>
    <div class="address">
      <svg width="11" height="16" viewBox="0 0 11 16"><path d="M5.5 0A5.5 5.5 0 0 0 0 5.5C0 9.6 5.5 16 5.5 16S11 9.6 11 5.5A5.5 5.5 0 0 0 5.5 0zm0 7.8a2.3 2.3 0 1 1 0-4.6 2.3 2.3 0 0 1 0 4.6z" fill="#fff"/></svg>
      <p>Calvorix Australia Pty Ltd<br>PO Box 4816<br>Coralbay BC<br>Queensland 4390</p>
    </div>
  </footer>
</div>
<p class="copyright">Copyright © 2015 calvorix.com.au. All Rights Reserved.</p>
</body>
</html>
```